HUMMING UNDER COPPER SKIES - A QUIET LEDGER

A5 size book of 190 - 210 (70 or 80 gsm wood free paper). The concept revolves around an unseen being that stands on a lotus flower who enters an Indian temple with many of his devotees. Traditional design with photography of a colourful Indian temple is preferred though alternative idea would also be considered. Short narratives at the back of book would give prospective readers an instantaneous insight into the story.

```html
<!DOCTYPE html>
<html lang="en">
<head>
<meta charset="utf-8">
<title>Humming under Copper Skies – Cover Spread</title>
<link rel="stylesheet" href="https://fonts.googleapis.com/css2?family=Kaushan+Script&family=EB+Garamond:ital@0;1&family=Cormorant+Garamond:ital,wght@1,400&family=Crimson+Text&display=swap">
<style>
  :root {
    --page: #ffffff;
    --backdrop: #ececec;
    --ink: #1d1d1d;
    --crimson: #c8124f;
    --rose: #e2305a;
    --orange: #f47a1c;
    --amber: #f7a21b;
    --plum: #5a2a4a;
  }
  * { margin: 0; padding: 0; box-sizing: border-box; }
  html, body { width: 899px; height: 1200px; overflow: hidden; background: var(--backdrop); }
  .canvas { position: relative; width: 899px; height: 1200px; }
  .spread {
    position: absolute; left: 0; top: 297px; width: 899px; height: 606px;
    background: var(--page); box-shadow: 0 2px 10px rgba(0,0,0,.12);
  }
  .back-cover { position: absolute; left: 0; top: 0; width: 416px; height: 100%; }
  .blurb {
    position: absolute; left: 56px; top: 62px; width: 327px;
    font-family: "Crimson Text", serif; font-size: 8.4px; line-height: 11.2px;
    color: var(--ink); text-align: justify; hyphens: auto;
  }
  .blurb p + p { margin-top: 11px; }
  .spine { position: absolute; left: 416px; top: 0; width: 56px; height: 100%; }
  .spine-title, .spine-author {
    position: absolute; left: 50%; writing-mode: vertical-rl; transform: translateX(-50%);
    white-space: nowrap;
  }
  .spine-title {
    top: 24px; font-family: "Kaushan Script", cursive; font-size: 23px;
    background: linear-gradient(180deg, var(--crimson), var(--rose) 45%, var(--amber));
    -webkit-background-clip: text; background-clip: text; color: transparent;
  }
  .spine-author {
    top: 350px; font-family: "Cormorant Garamond", serif; font-style: italic;
    font-size: 26px; letter-spacing: 10px; color: var(--ink);
  }
  .front-cover { position: absolute; left: 472px; top: 0; width: 427px; height: 100%; }
  .title {
    position: absolute; left: 20px; right: 20px; top: 30px; text-align: center;
    font-family: "Kaushan Script", cursive; line-height: .95;
    background: linear-gradient(180deg, var(--crimson) 10%, var(--rose) 45%, var(--orange) 80%, var(--amber));
    -webkit-background-clip: text; background-clip: text; color: transparent;
  }
  .title .line-1 { display: block; font-size: 58px; }
  .title .line-2 { display: block; font-size: 38px; margin-top: -4px; }
  .title .line-3 { display: block; font-size: 52px; margin-top: -2px; }
  .subtitle {
    position: absolute; right: 58px; top: 208px;
    font-family: "EB Garamond", serif; font-style: italic; font-size: 20px; color: var(--ink);
  }
  .temple-photo {
    position: absolute; left: 20px; top: 250px; width: 382px; height: 188px;
  }
  .author {
    position: absolute; left: 0; right: 0; top: 508px; text-align: center;
    font-family: "Cormorant Garamond", serif; font-style: italic; font-size: 34px;
    letter-spacing: 11px; color: var(--ink);
  }
</style>
</head>
<body>
<div class="canvas">
  <section class="spread">
    <div class="back-cover">
      <div class="blurb">
        <p>Lorem ipsum dolor sit amet, consectetur adipiscing elit. Mauris nec sodales tortor, in sollicitudin ipsum. Sed cursus ut libero ac iaculis. Pellentesque in est non nulla sollicitudin feugiat sit amet a augue. Etiam nec ligula fringilla, ultrices lacus sed, posuere velit. Etiam eget turpis felis. Aliquam lorem nunc, semper elementum venenatis ac, bibendum nec justo. Fusce id orci dictum, accumsan tellus et, dignissim metus. Quisque tortor arcu, sagittis quis nunc at, tristique rutrum ligula. Maecenas tincidunt est ac metus malesuada porta. Etiam scelerisque rhoncus elit, vitae interdum metus consequat iaculis. Cras in neque congue, dignissim mauris vitae, lobortis felis. Suspendisse consectetur rutrum tortor. Vestibulum lobortis nibh non congue elementum. Ut feugiat velit nisi, ac aliquet ante feugiat commodo. Sed porttitor odio nec egestas ultrices.</p>
        <p>Vestibulum mollis feugiat neque malesuada elementum. Vivamus maximus semper lorem non laoreet. Quisque lobortis diam odio, eget elementum lorem tempus a. Praesent id faucibus nulla, ac dignissim leo. Etiam auctor porta consequat. In quis justo ante. Suspendisse quis eros nulla. Sed suscipit eu arcu eget tempor. Aenean imperdiet mauris in tellus sagittis, eget commodo turpis molestie. Vestibulum ante ipsum primis in faucibus orci luctus et ultrices posuere cubilia Curae; Aenean pharetra in ex eu lobortis. Nullam ac bibendum nibh.</p>
        <p>Etiam mi mauris, sagittis id semper et, blandit id elit. Praesent luctus tempor diam ullamcorper imperdiet. Vestibulum velit magna, pellentesque in arcu at, vehicula mattis dui. Nulla facilisi. Cras gravida posuere dapibus. Quisque sed est elit. Vestibulum arcu justo, tristique ut sem et, tempus maximus nisi. Duis fringilla, leo vel vehicula cursus, ipsum nulla eleifend est, ac pretium leo justo et nibh. Maecenas quam turpis, ullamcorper eu arcu a, iaculis cursus magna. Fusce ultrices auctor eros, ut varius felis rhoncus pretium. Donec tincidunt augue ac felis placerat congue. Phasellus elementum commodo metus ac aliquet. Lorem ipsum dolor sit amet, consectetur adipiscing elit. Nulla pretium, nisi faucibus tempor interdum, nulla magna malesuada tortor, a suscipit mauris elit vitae ex. Nam vel eros pellentesque quam auctor tempor non in nisi. Integer cursus ante diam, in laoreet eros tempus sed.</p>
      </div>
    </div>

    <div class="spine">
      <div class="spine-title">Humming under Copper Skies</div>
      <div class="spine-author">Author Name</div>
    </div>

    <div class="front-cover">
      <h1 class="title">
        <span class="line-1">Humming</span>
        <span class="line-2">under</span>
        <span class="line-3">Copper Skies</span>
      </h1>
      <div class="subtitle">A Quiet Ledger</div>
      <svg class="temple-photo" viewBox="0 0 382 188" role="img" aria-label="Photograph of a carved Indian stone temple, tinted orange to crimson, with brushed edges">
        <defs>
          <linearGradient id="templeTint" x1="0" y1="0" x2="0" y2="1">
            <stop offset="0" stop-color="#f7a21b"/>
            <stop offset=".3" stop-color="#f0602a"/>
            <stop offset=".6" stop-color="#d9254e"/>
            <stop offset=".88" stop-color="#5a2a4a"/>
            <stop offset="1" stop-color="#ffffff"/>
          </linearGradient>
        </defs>
        <path fill="url(#templeTint)" d="M40 40 L110 28 L150 8 L232 8 L272 28 L342 40 L372 70 L366 100 L380 130 L356 170 L300 182 L190 186 L80 182 L20 170 L4 130 L16 100 L8 70 Z"/>
      </svg>
      <div class="author">Author Name</div>
    </div>
  </section>
</div>
</body>
</html>
```